Alaska Outdoor Adventure Tour Company Flyer

We need a cutting edge flyer design that stands out above the rest. We are a tour company offering a variety of services. We would like two Dual sided flyers. One on Ice Fishing/Sledding/Snow Shoeing Only, One on Aurora viewing / Hot Springs Aurora Viewing, and the third we would like a to be a tri-fold flyer including all the activities listed above. We are trying to drive traffic to our website and phones for bookings. We of course want to push that we are the best most trusted tour/experience company in Alaska. We are on stay nook as well as JourneyRater and would like to include there logo as well as our own logo on all the flyers. I have attached photos of all of our competitors flyers. Here is our website https://www.brantholmlodges.info/
Here is our listings on Stay Nook
https://www.staynook.com/experiences/5920417?s=67&shared_item_type=2&virality_entry_point=2&sharer_id=31947260

https://www.staynook.com/experiences/5926083?s=67&shared_item_type=2&virality_entry_point=2&sharer_id=31947260

https://www.staynook.com/experiences/5948216?s=67&shared_item_type=2&virality_entry_point=2&sharer_id=31947260

https://www.staynook.com/experiences/5951739?s=67&shared_item_type=2&virality_entry_point=2&sharer_id=31947260

Here is our Chatterloop Page
https://www.chatterloop.com/Brantholm-Lodges-275194038816257/?ref=bookmarks

Target Market(s)

Japanese travelers and Chinese travelers. Our other market is travelers from New York, and California.

Industry/Entity Type

Tourism

Colors

Designer to choose colors to be used in the design.

Requirements
Must have
• Company Logo more prominent than the Stay Nook and JourneyRater logo. Website adress and phone number. Include of our best photos from our website or Stay nook page.
• Must be the long narrow flyer design. Either two sided design or tri-fold design
Nice to have
• Possibly some of the key titles in Japanese or Chinese. Hopping our flyers will stand out from the rest. bright new agey but Alaskan. Hopping for something really cool and cutting edge. PRICE MATCH GUARANTY

```html
<!DOCTYPE html>
<html lang="en">
<head>
<meta charset="utf-8">
<title>Brantholm Lodges – Tri-fold Flyer</title>
<link rel="stylesheet" href="https://fonts.googleapis.com/css2?family=Oswald:wght@400;500;600&family=Roboto:wght@300;400&family=Noto+Sans+SC:wght@500&display=swap">
<style>
:root{
  --gold:#b99b5f;
  --gold-light:#d9c08a;
  --ink:#141414;
  --slate:#262626;
  --paper:#ffffff;
  --text-dark:#333333;
  --text-light:#e8e8e8;
  --stage:#ffffff;
}
*{box-sizing:border-box;margin:0;padding:0}
html,body{width:1200px;height:1000px;overflow:hidden;background:var(--stage)}
body{position:relative;font-family:"Roboto",Arial,sans-serif}
.spread{position:absolute;left:296px;width:608px;height:470px;display:flex;box-shadow:0 4px 10px rgba(0,0,0,.25)}
.spread--outside{top:15px}
.spread--inside{top:503px}
.panel{position:relative;width:203px;height:100%;overflow:hidden}
.panel:nth-child(2){width:202px}
.bg{position:absolute;inset:0;width:100%;height:100%}
.heading{font-family:"Oswald",Arial,sans-serif;font-weight:500;color:var(--gold);text-transform:uppercase;letter-spacing:.3px}
.zh{font-family:"Noto Sans SC",sans-serif;font-weight:500}
.body-copy{font-size:7.4px;line-height:1.45;font-weight:300}

/* outside – tours panel */
.panel--tours{background:var(--paper)}
.tours{position:absolute;left:14px;top:18px}
.tours .heading{font-size:13px;margin-bottom:8px}
.tours li{list-style:none;font-size:8px;color:var(--text-dark);margin-bottom:7.2px;padding-left:18px;position:relative}
.tours li::before{content:"";position:absolute;left:7px;top:2px;width:4px;height:4px;border-top:1.2px solid var(--text-dark);border-right:1.2px solid var(--text-dark);transform:rotate(45deg)}
.about{position:absolute;left:14px;right:14px;top:260px;color:var(--text-light)}
.about .heading{font-size:12px;margin-bottom:7px}
.about .tagline{font-size:8px;margin-bottom:7px}

/* outside – contact panel */
.panel--contact{color:var(--ink)}
.aurora{position:absolute;left:0;top:0;width:100%;height:345px;background:linear-gradient(170deg,#cfc59a 0%,#b7c08a 30%,#a6b07a 55%,#8c8a62 80%,#5e5940 100%)}
.section-title{display:flex;align-items:center;gap:8px;justify-content:center;font-size:12px;color:var(--ink)}
.section-title::before,.section-title::after{content:"";height:1px;width:48px;background:#6b6544}
.contact{position:absolute;left:0;right:0;top:20px;text-align:center}
.contact-item{margin-top:12px;font-size:8px;color:#2a2a2a}
.icon-dot{width:11px;height:11px;border-radius:50%;background:#6e6a4c;margin:0 auto 5px;display:flex;align-items:center;justify-content:center}
.follow{position:absolute;left:0;right:0;top:213px;text-align:center}
.book{position:absolute;left:0;right:0;top:356px;text-align:center}
.book .heading{font-size:12px;color:var(--gold-light)}
.partner-name{display:flex;align-items:center;justify-content:center;gap:6px;margin-top:12px;font-family:"Oswald",Arial,sans-serif;font-weight:500;font-size:20px;color:#e0565b}
.partner-name i{width:11px;height:11px;border-radius:50%;background:#e0565b;display:block}
.stars{margin-top:6px;color:#f2c94c;font-size:11px;letter-spacing:1px}

/* outside – cover panel */
.panel--cover{background:var(--ink)}
.brand{position:absolute;left:0;right:0;top:56px;text-align:center;display:flex;flex-direction:column;align-items:center}
.brand-mark{width:40px;height:40px;border-radius:50%;border:1.5px solid var(--gold);margin-bottom:8px}
.brand-name{font-family:"Oswald",Arial,sans-serif;font-weight:400;font-size:14px;letter-spacing:1.5px;color:var(--gold);line-height:1.1}
.cover-photo{position:absolute;left:0;top:0;width:100%;height:100%}
.cover-tagline{position:absolute;left:16px;bottom:28px}
.cover-tagline .heading{font-size:12.5px;color:var(--gold-light);line-height:1.35}
.cover-tagline .zh{font-size:11px;color:var(--gold-light);margin-top:2px}

/* inside – activity cards */
.card-col{display:flex;flex-direction:column}
.card{position:relative;height:235px;overflow:hidden;background:var(--ink)}
.card-body{position:absolute;left:14px;right:10px;top:130px;color:var(--text-light)}
.card-title{font-family:"Oswald",Arial,sans-serif;font-weight:500;font-size:12.5px;line-height:1.1;color:#f3ecd9;text-transform:uppercase}
.card-title .zh{display:block;font-size:11px;color:var(--gold-light);margin-top:1px}
.card .body-copy{margin-top:6px;font-size:7px}
.price{position:absolute;width:34px;height:34px;border-radius:50%;background:#6d5f40;color:#fff;display:flex;flex-direction:column;align-items:center;justify-content:center;font-family:"Oswald",Arial,sans-serif;font-size:11px;line-height:1}
.price small{font-size:5px;margin-top:1px}
.card .price{right:14px;top:128px}

/* inside – aurora tours panel */
.panel--aurora{background:var(--paper)}
.tour{position:absolute;left:16px;right:12px;color:var(--text-dark)}
.tour .heading{font-size:12.5px;color:#6c5b37;line-height:1.1}
.tour .zh{font-size:11px;color:#6c5b37;margin-top:1px}
.tour .pickup{font-size:7px;margin-top:7px;letter-spacing:.2px}
.tour .body-copy{margin-top:6px;font-size:7px}
.tour .price{right:0;top:0}
.tour--aurora{top:20px}
.tour--springs{top:138px}
.springs-photo{position:absolute;left:0;bottom:0;width:100%;height:165px;background:linear-gradient(180deg,rgba(255,255,255,0) 0%,#b6c3e4 25%,#7d8fc9 65%,#5a6cb0 100%)}
.footer-link{position:absolute;left:14px;bottom:8px;font-size:7px;color:#fff;letter-spacing:.2px}
</style>
</head>
<body>

<!-- Outside spread -->
<section class="spread spread--outside">
  <div class="panel panel--tours">
    <svg class="bg" viewBox="0 0 203 470" preserveAspectRatio="none" aria-hidden="true">
      <polygon points="0,186 203,226 203,236 0,196" fill="#b99b5f"/>
      <polygon points="0,196 203,236 203,470 0,470" fill="#2b2b2b"/>
    </svg>
    <div class="tours">
      <h2 class="heading">Tours</h2>
      <ul>
        <li>Alaska Ice Fishing</li>
        <li>Thrilling Sledding Adventure</li>
        <li>Snow Shoeing Adventure</li>
        <li>Incredible Aurora Viewing</li>
        <li>Hot Springs Aurora Viewing</li>
        <li>Magical Drive Through Light Show</li>
        <li>Micro Brewery/ Distillery Night</li>
      </ul>
    </div>
    <div class="about">
      <h2 class="heading">About Us</h2>
      <p class="tagline">The Travel Experts in Fairbanks AK</p>
      <p class="body-copy">We are passionate outdoor enthusiasts and naturalists. My wife and I were born and raised in Alaska and love it here. My wife works at medical clinic and I work as a carpenter. We spend our off time in the great outdoors enjoying all Alaska has to offer. We love to share our love and knowledge of Alaska by taking people out on memorable experiences. Here at Brantholm Lodges, LLC will help you fine the best Ice Fishing, incredible AURORA views, Snowshoing, Sledding, and much more.</p>
    </div>
  </div>

  <div class="panel panel--contact">
    <div class="aurora" role="img" aria-label="Green and gold northern lights over a dark winter sky"></div>
    <svg class="bg" viewBox="0 0 202 470" preserveAspectRatio="none" aria-hidden="true">
      <polygon points="0,330 202,310 202,470 0,470" fill="#1a1a1a"/>
    </svg>
    <div class="contact">
      <h2 class="heading section-title">Contact Us</h2>
      <div class="contact-item"><div class="icon-dot"><svg width="6" height="6" viewBox="0 0 10 10"><path d="M2 1l2 2-1 1.5c.8 1.5 1.8 2.5 3 3L7.5 6l2 2-1.5 1.5C4 9 1 6 .5 1.5z" fill="#fff"/></svg></div>907-555-0148</div>
      <div class="contact-item"><div class="icon-dot"><svg width="6" height="5" viewBox="0 0 10 8"><rect x=".5" y=".5" width="9" height="7" fill="none" stroke="#fff"/><path d="M.5.5L5 4.5 9.5.5" fill="none" stroke="#fff"/></svg></div>ada@907bln.com</div>
      <div class="contact-item"><div class="icon-dot"><svg width="6" height="6" viewBox="0 0 10 10"><circle cx="5" cy="5" r="4.2" fill="none" stroke="#fff"/><path d="M1 5h8M5 1c-2 2.5-2 5.5 0 8M5 1c2 2.5 2 5.5 0 8" fill="none" stroke="#fff" stroke-width=".8"/></svg></div>www.brantholmlodges.info</div>
      <div class="contact-item"><div class="icon-dot"><svg width="5" height="7" viewBox="0 0 8 11"><path d="M4 11S0 6 0 4a4 4 0 018 0c0 2-4 7-4 7z" fill="#fff"/></svg></div>Fairbanks, United States</div>
    </div>
    <div class="follow">
      <h2 class="heading section-title">Follow Us!</h2>
      <div class="contact-item"><div class="icon-dot"></div>Brantholm Lodges</div>
    </div>
    <div class="book">
      <h2 class="heading">Book Your Tour Now!</h2>
      <div class="partner-name"><i></i>Stay Nook</div>
      <div class="stars">★★★★★</div>
    </div>
  </div>

  <div class="panel panel--cover">
    <svg class="cover-photo" viewBox="0 0 203 470" preserveAspectRatio="none" aria-hidden="true">
      <defs>
        <linearGradient id="lakeDusk" x1="0" y1="0" x2="0" y2="1">
          <stop offset="0" stop-color="#3c4f9a"/>
          <stop offset=".45" stop-color="#7a86c8"/>
          <stop offset=".7" stop-color="#5a4b9c"/>
          <stop offset="1" stop-color="#2b2f6e"/>
        </linearGradient>
      </defs>
      <polygon points="203,0 203,14 150,0" fill="#b99b5f"/>
      <polygon points="0,120 203,190 203,200 0,130" fill="#b99b5f"/>
      <polygon points="0,130 203,200 203,345 0,420" fill="url(#lakeDusk)" role="img" aria-label="Steaming hot spring pool among snowy trees at dusk"/>
      <polygon points="0,420 203,345 203,355 0,430" fill="#b99b5f"/>
      <circle cx="172" cy="360" r="22" fill="#c4a14a"/>
      <circle cx="172" cy="360" r="16" fill="#8c1f1f"/>
    </svg>
    <div class="brand">
      <div class="brand-mark"></div>
      <div class="brand-name">BRANTHOLM<br>LODGES</div>
    </div>
    <div class="cover-tagline">
      <h2 class="heading">Taking You<br>Where You Want To Go</h2>
      <p class="zh">带你去你想去的地方</p>
    </div>
  </div>
</section>

<!-- Inside spread -->
<section class="spread spread--inside">
  <div class="panel card-col">
    <article class="card">
      <svg class="bg" viewBox="0 0 203 235" preserveAspectRatio="none" aria-hidden="true">
        <rect width="203" height="150" fill="#6f7f9a" role="img" aria-label="Angler holding a fresh catch on a frozen lake"/>
        <polygon points="0,150 203,95 203,235 0,235" fill="#141414"/>
        <polygon points="0,150 203,95 203,99 0,154" fill="#b99b5f"/>
      </svg>
      <div class="price">$128<small>2 HRS</small></div>
      <div class="card-body">
        <h3 class="card-title">Alaska<br>Ice Fishing<span class="zh">阿拉斯加冰钓</span></h3>
        <p class="body-copy">Join me ice fishing on Tanana lakes a few minutes from town. Everything needed will be provided. I will take you through the steps on how to catch Alaska Pike &amp; Grayling fish all from the warmth of the ice house. Snacks and hot chocolate will also be provided.</p>
      </div>
    </article>
    <article class="card">
      <svg class="bg" viewBox="0 0 203 235" preserveAspectRatio="none" aria-hidden="true">
        <rect width="203" height="150" fill="#3a3a4a" role="img" aria-label="Friends on sleds on a snowy hill at night"/>
        <polygon points="0,150 203,95 203,235 0,235" fill="#141414"/>
        <polygon points="0,150 203,95 203,99 0,154" fill="#b99b5f"/>
      </svg>
      <div class="price">$45<small>2 HRS</small></div>
      <div class="card-body">
        <h3 class="card-title">Thrilling<br>Sledding Adventure<span class="zh">颠抖的冒险</span></h3>
        <p class="body-copy">Sledding is one of Alaska's most thrilling sports. We will go over sledding basics and how to steer the sled as your gliding down the hill. Once you feel comfortable you can enjoy racing your friends down the hill.</p>
      </div>
    </article>
  </div>

  <div class="panel card-col">
    <article class="card">
      <svg class="bg" viewBox="0 0 202 235" preserveAspectRatio="none" aria-hidden="true">
        <rect width="202" height="150" fill="#8aa0c4" role="img" aria-label="Snowshoers on a bright snowy forest trail"/>
        <polygon points="0,150 202,95 202,235 0,235" fill="#141414"/>
        <polygon points="0,150 202,95 202,99 0,154" fill="#b99b5f"/>
      </svg>
      <div class="price">$85<small>2 HRS</small></div>
      <div class="card-body">
        <h3 class="card-title">Snowshoe<br>Adventure<span class="zh">雪花冒险</span></h3>
        <p class="body-copy">Snowshoeing is a great way to explore the wilderness and experience all of Alaska's natural beauty. Enjoy a beautiful Snowshoe Journy through trails along the Tanana River and through a historic Alaska village on the hillside where you will see a living style of years past.</p>
      </div>
    </article>
    <article class="card">
      <svg class="bg" viewBox="0 0 202 235" preserveAspectRatio="none" aria-hidden="true">
        <rect width="202" height="150" fill="#4a2f55" role="img" aria-label="Tunnel of colourful holiday lights over a road at night"/>
        <polygon points="0,150 202,95 202,235 0,235" fill="#141414"/>
        <polygon points="0,150 202,95 202,99 0,154" fill="#b99b5f"/>
      </svg>
      <div class="price">$45<small>1 HR</small></div>
      <div class="card-body">
        <h3 class="card-title">Magical Drive<br>Through Light Show<span class="zh">通过光影展示的磁力驱动</span></h3>
        <p class="body-copy">Enjoy viewing the beautiful lights from the warm comfort of our luxury coach. Travel to and from your hotel is included!</p>
      </div>
    </article>
  </div>

  <div class="panel panel--aurora">
    <svg class="bg" viewBox="0 0 203 470" preserveAspectRatio="none" aria-hidden="true">
      <polygon points="0,0 203,0 203,12 150,0 0,0" fill="#141414"/>
      <polygon points="120,0 203,0 203,10" fill="#b99b5f"/>
    </svg>
    <div class="tour tour--aurora">
      <div class="price">$120<small>2 HRS</small></div>
      <h3 class="heading">Incredible<br>Aurora Viewing</h3>
      <p class="zh">令人难以置信的极光观看</p>
      <p class="pickup">FREE GUEST PICKUP FROM 4:15PM TO 5PM.</p>
      <p class="body-copy">From our unique vantage point at the top of Cleary Summit, overlooking the Poker Flat Research Range, we boast the best view of the dark night sky within a 30-minute drive of Fairbanks.</p>
    </div>
    <div class="tour tour--springs">
      <div class="price">$85<small>11 HRS</small></div>
      <h3 class="heading">Hot Springs<br>Aurora Viewing</h3>
      <p class="zh">温泉极光观赏</p>
      <p class="body-copy">Our Birchwater Hot Springs / Northern Lights Alaska Tours begin right at your Fairbanks hotel, so you don't need to plan how to get to us and you will save additional taxi costs.</p>
      <p class="pickup">FREE GUEST PICKUP FROM 4:15PM TO 5PM</p>
      <p class="body-copy">Enjoy the mineral hot springs in a beautiful natural setting and experience the dancing of the northern lights.</p>
      <p class="body-copy">The world's largest year-round ice museum is your first stop at Birchwater Resort. Created from over 1,000 tons of ice and snow the ice museum contains spectacular ice carvings for your enjoyment.</p>
      <p class="body-copy">Along the way we almost always spot moose.</p>
    </div>
    <div class="springs-photo" role="img" aria-label="Guest relaxing in a steaming outdoor hot spring under blue winter light"></div>
    <p class="footer-link">MORE INFORMATION AT www.brantholmlodges.info</p>
  </div>
</section>

</body>
</html>
```